Wild Harbor Realm Banner Ad

I Host a Server for Stoneforge. Its called Wild Harbor Realm.
I am looking for a catchy banner Ad that shows that we are clearly a Stoneforge server and we are fun for all ages. The server has plugins that adds different mechanics to the game, mechanics we have are listed on the picture added to this project.
If you don't know stone forge. I suggest you watch the video on Stoneforge.net. But the basis of the game is you can break blocks, mine ores, and build huge structures out of what you collect.
Our Current Website is www.wildharborrealm.com
And if you have Stoneforge and would like to see the basis of our server its mc.wildharborrealm.com.
Like i said i would like the logo to have a Stoneforge feel, and show who we are.
Thanks for you're time.
Reason: We do not need this project right away anymore, so more chances for submissions.
Thanks
Industry/Entity Type
Build
Logo Text
WHR or Wild Harbor Realm
Requirements
Must have
- Must have IP address mc.wildharborrealm.com
Nice to have
- Something to show we are Stoneforge related and have Economy so some sort of Money aspect. We are from Canada so if you can work that in too.
The size needed is 468x60 px

```html
<!DOCTYPE html>
<html lang="en">
<head>
<meta charset="utf-8">
<title>Wild Harbor Realm Banner Ads</title>
<link rel="stylesheet" href="https://fonts.googleapis.com/css2?family=Open+Sans:wght@600;700;800&display=swap">
<style>
  :root {
    --stage: #646567;
    --blue-deep: #0a2fa8;
    --blue-mid: #1347d6;
    --blue-panel: #0a55e6;
    --wood-dark: #3a2a1c;
    --wood-mid: #5b4331;
    --title-cream: #f3d9a4;
    --ip-blue: #b9cbf0;
    --ip-blue-dark: #6fa0f0;
    --prize-gold: #f2c230;
    --feature-white: #ffffff;
  }
  * { margin: 0; padding: 0; box-sizing: border-box; }
  html, body { width: 1200px; height: 900px; overflow: hidden; }
  body {
    background: var(--stage);
    font-family: "Open Sans", Arial, sans-serif;
    position: relative;
  }
  .banner {
    position: absolute;
    left: 249px;
    width: 702px;
    height: 90px;
    overflow: hidden;
  }
  .banner--blue { top: 345px; background: linear-gradient(100deg, var(--blue-deep), var(--blue-mid) 60%, var(--blue-deep)); }
  .banner--wood { top: 465px; }
  .banner__bg { position: absolute; inset: 0; }
  .wood-fill {
    position: absolute; inset: 0;
    background: linear-gradient(180deg, var(--wood-mid), var(--wood-dark) 55%, var(--wood-mid));
  }
  .banner__title {
    position: absolute;
    left: 18px; top: 12px;
    font-size: 33px;
    font-weight: 800;
    letter-spacing: 0.5px;
    color: var(--title-cream);
    text-transform: uppercase;
    white-space: nowrap;
  }
  .banner__ip {
    position: absolute;
    left: 21px; top: 57px;
    font-size: 19px;
    font-weight: 700;
    color: var(--ip-blue);
  }
  .banner--wood .banner__ip { color: var(--ip-blue-dark); }
  .banner__prizes {
    position: absolute;
    left: 303px; top: 60px;
    font-size: 14px;
    font-weight: 700;
    color: var(--prize-gold);
    text-transform: uppercase;
  }
  .banner__prizes .dollar { font-size: 17px; margin-right: 6px; }
  .features {
    position: absolute;
    left: 480px; top: 6px;
    list-style: none;
    color: var(--feature-white);
    font-size: 16px;
    font-weight: 600;
    line-height: 25.5px;
    white-space: nowrap;
  }
  .features li:nth-child(2) { padding-left: 5px; }
  .features li:nth-child(3) { padding-left: 8px; }
  .features .sep { margin: 0 8px; }
</style>
</head>
<body>
  <div class="banner banner--blue">
    <svg class="banner__bg" width="702" height="90" viewBox="0 0 702 90" aria-hidden="true">
      <defs>
        <linearGradient id="panelGlow" x1="0" y1="0" x2="1" y2="0">
          <stop offset="0" stop-color="#1a6cff"/>
          <stop offset="1" stop-color="#0a3fc4"/>
        </linearGradient>
      </defs>
      <polygon points="488,0 702,0 702,90 474,90" fill="url(#panelGlow)"/>
    </svg>
    <div class="banner__title">Wild Harbor Realm</div>
    <div class="banner__ip">mc.wildharborrealm.com</div>
    <div class="banner__prizes"><span class="dollar">$</span>Monthly Prizes</div>
    <ul class="features">
      <li>Survival Games</li>
      <li>MiniGames<span class="sep">I</span>SKILLRPG</li>
      <li>MultiRealm<span class="sep">I</span>No Griefing</li>
    </ul>
  </div>

  <div class="banner banner--wood">
    <div class="wood-fill" role="img" aria-label="Background of dark wooden block texture"></div>
    <div class="banner__title">Wild Harbor Realm</div>
    <div class="banner__ip">mc.wildharborrealm.com</div>
    <div class="banner__prizes"><span class="dollar">$</span>Monthly Prizes</div>
    <ul class="features">
      <li>Survival Games</li>
      <li>MiniGames<span class="sep">I</span>SKILLRPG</li>
      <li>MultiRealm<span class="sep">I</span>No Griefing</li>
    </ul>
  </div>
</body>
</html>
```